Business Card design for insurance broker in Denver, CO, USA

I need a business card designed using this logo that was just created. We sell life and disability income insurance to US consumers.
Looking for a professionally designed card to make use of the logo and have something to hand to prospects or new business referral sources. The card could be white, gray, black or whatever you would recommend.

Target Market(s)

US Consumers and other financial professionals that I partner with.

Industry/Entity Type

Insurance Broker

Contact Information for Business Card

Owen R. Tessler, CLU, LUTCF (please note that CLU should have a superscript R in a circle for registered trademark)
President
phone (303) 555-0147
email owen@brightlakecoverage.com
4620 W. Hollister Rd, Suite 310, Cedar Bluff, CO 80999
Somewhere fit in a tagline saying "Your resource for life, long term care, and disability insurance" (maybe the back if it doesn't fit on the front, your call)

Font styles to use
Sans Serif

Requirements
Must have
• Must have logo in correct blue and gray colors, my name, address, phone, email. Order and placement determined by the designer.
• I just want something that looks a more professional than what I could have done using the business card designer tool on printmakerhub.com or CardNest, or any other do-it-yourself tool
• A regular rectangular business card with square corners is preferred
Nice to have
• I included the logos of 2 organizations I belong to (GQLF and BEPWO). They should be small, but visible on the back only. If it doesn’t look good, this is not a requirement, feel free to drop it.
Should not have
• Do not add any colors not already in the logo, except use of black and whites which are okay. If you use the logo on the back and want to make that in all black, gray or white, that may be okay as well.

```html
<!DOCTYPE html>
<html lang="en">
<head>
<meta charset="utf-8">
<title>Brightlake Coverage – Business Card</title>
<link href="https://fonts.googleapis.com/css2?family=Montserrat:wght@400;500;600;700&display=swap" rel="stylesheet">
<style>
  :root {
    --brand-blue: #2f8ad0;
    --brand-gray: #9a9a9c;
    --ink: #4a4a4c;
    --back-dark: #3e3e40;
    --back-mid: #5b5b5d;
    --canvas: #ececec;
    --white: #ffffff;
  }
  * { margin: 0; padding: 0; box-sizing: border-box; }
  html, body { width: 1200px; height: 929px; overflow: hidden; }
  body {
    background: var(--canvas);
    font-family: "Montserrat", Arial, sans-serif;
    position: relative;
  }
  .card {
    position: absolute;
    width: 560px;
    height: 320px;
    border-radius: 22px;
    overflow: hidden;
    box-shadow: 0 12px 30px rgba(0,0,0,0.18);
  }

  /* Back of card */
  .card-back {
    left: 110px; top: 90px;
    background: radial-gradient(ellipse at 55% 35%, var(--back-mid), var(--back-dark) 80%);
  }
  .world-map-area {
    position: absolute;
    left: 60px; top: 40px; width: 440px; height: 240px;
    border-radius: 40%;
    background: radial-gradient(ellipse at center, rgba(120,120,122,0.35), rgba(120,120,122,0) 70%);
  }
  .back-logo {
    position: absolute;
    inset: 0;
    display: flex; align-items: center; justify-content: center; gap: 16px;
  }
  .back-logo .logo-ring {
    width: 62px; height: 62px; border-radius: 50%;
    border: 5px solid var(--white);
  }
  .back-logo .logo-name {
    color: var(--white);
    font-weight: 600;
    font-size: 36px;
    letter-spacing: 1px;
    text-transform: uppercase;
    line-height: 1;
  }

  /* Front of card */
  .card-front {
    left: 530px; top: 500px;
    background: var(--white);
  }
  .front-logo {
    position: absolute;
    right: 34px; top: 28px;
    display: flex; align-items: center; gap: 12px;
  }
  .front-logo .logo-ring {
    width: 46px; height: 46px; border-radius: 50%;
    border: 4px solid var(--brand-blue);
  }
  .front-logo .logo-name {
    color: var(--brand-blue);
    font-weight: 600;
    font-size: 25px;
    letter-spacing: 0.5px;
    text-transform: uppercase;
  }
  .contact {
    position: absolute;
    left: 34px; top: 106px;
    color: var(--ink);
  }
  .person-name {
    color: var(--brand-blue);
    font-weight: 600;
    font-size: 24px;
    line-height: 1.1;
  }
  .person-name sup { font-size: 10px; font-weight: 500; }
  .person-title {
    font-weight: 600;
    font-size: 17px;
    line-height: 1.2;
    margin-bottom: 8px;
  }
  .address { font-size: 14px; line-height: 1.35; margin-bottom: 5px; }
  .contact-line {
    display: flex; align-items: center; gap: 7px;
    font-size: 14px; line-height: 1.5;
  }
  .contact-line svg { width: 13px; height: 13px; flex: none; }
  .badges {
    position: absolute;
    right: 34px; top: 196px;
    display: flex; align-items: flex-end; gap: 14px;
  }
  .badge-circle {
    width: 38px; height: 38px; border-radius: 50%;
    background: var(--brand-blue); opacity: 0.8;
  }
  .badge-square {
    width: 38px; height: 38px; background: var(--ink);
  }
  .tagline-band {
    position: absolute;
    left: 0; right: 0; bottom: 0; height: 38px;
    background: var(--brand-blue);
    color: var(--white);
    display: flex; align-items: center; justify-content: center;
    font-weight: 600; font-size: 12.5px; letter-spacing: 0.3px;
    text-transform: uppercase;
  }
</style>
</head>
<body>

  <section class="card card-back" aria-label="Card back">
    <div class="world-map-area" role="img" aria-label="Faint world map backdrop"></div>
    <div class="back-logo">
      <span class="logo-ring"></span>
      <span class="logo-name">Brightlake<br>Coverage</span>
    </div>
  </section>

  <section class="card card-front" aria-label="Card front">
    <div class="front-logo">
      <span class="logo-ring"></span>
      <span class="logo-name">Brightlake Coverage</span>
    </div>

    <div class="contact">
      <div class="person-name">Owen R. Tessler, CLU<sup>®</sup>, LUTCF</div>
      <div class="person-title">President</div>
      <div class="address">4620 W. Hollister Rd, Suite 310,<br>Cedar Bluff, CO 80999</div>
      <div class="contact-line">
        <svg viewBox="0 0 12 12" aria-hidden="true"><path d="M2.5 1 L4.5 1 L5.3 3.6 L4 4.6 Q5 7 7.4 8 L8.4 6.7 L11 7.5 L11 9.5 Q10.5 11 9 11 Q1 10 1 3 Q1 1.5 2.5 1 Z" fill="var(--brand-blue)"/></svg>
        (303) 555-0147
      </div>
      <div class="contact-line">
        <svg viewBox="0 0 12 12" aria-hidden="true"><rect x="0.8" y="2.3" width="10.4" height="7.4" fill="none" stroke="var(--brand-blue)" stroke-width="1.2"/><path d="M1 2.6 L6 6.6 L11 2.6" fill="none" stroke="var(--brand-blue)" stroke-width="1.2"/></svg>
        owen@brightlakecoverage.com
      </div>
      <div class="contact-line">
        <svg viewBox="0 0 12 12" aria-hidden="true"><circle cx="6" cy="6" r="5" fill="none" stroke="var(--brand-blue)" stroke-width="1.2"/><ellipse cx="6" cy="6" rx="2.2" ry="5" fill="none" stroke="var(--brand-blue)" stroke-width="1"/><line x1="1" y1="6" x2="11" y2="6" stroke="var(--brand-blue)" stroke-width="1"/></svg>
        www.brightlakecoverage.com
      </div>
    </div>

    <div class="badges" aria-label="Membership badges">
      <span class="badge-circle"></span>
      <span class="badge-square"></span>
    </div>

    <div class="tagline-band">Your resource for life, long term care, and disability insurance</div>
  </section>

</body>
</html>
```